BrelloVista.com

3D Advertising Agency. We Bring Brands to Life! We provide the most advanced No Glasses Needed 3D digital displays for advertising. Our multi-media experts produce the most stunning and impressive advertising for brands in 3D and consumers get the experience of a lifetime when they see our displays Without Glasses! The website need to look eye-catching, creative and vibrant! Our glasses free 3D displays leave a long lasting impression and create the ultimate consumer experience! We need to look BIG, we need to look INNOVATIVE, CUTTING EDGE and ready to deliver. Please see website examples in comments section. http://pruvangroup.co.uk/ has nice wire frame.
http://www.halvornestudio.com/media/sports.html has good secondary content page layouts and calls to action.
Updates

Take a look at this design and content.  This is my competition. http://www.kelbrapanel.com/About+Us

http://www.somvardeck.com/

competitor

This company http://www.tremnikoptic.com/ is my partner and I am a reseller for them.  I don't want to look like them 100%, they manufacture, we are a solutions provider.

MAKE ME LOOK LIKE THIS! http://pruvangroup.co.uk/

TOP NAVIGATION SHOULD ONLY INCLUDE THESE:

SOLUTION, MEDIA, SERVICES, ABOUT US

Target Market(s)

Casinos, NightClubs, bars, movie theaters,Fortune 500 consumer brands, Entertainment, Sports and Fashion Leaders.

Industry/Entity Type

Advertising

Requirements
Must have
• 3D effects, Flash, Dynamic imagery, clean and not too busy!
Nice to have
• Must make our logo's color symbol come to life with flash.

```html
<!DOCTYPE html>
<html lang="en">
<head>
<meta charset="utf-8">
<title>BrelloVista — We Bring Brands to Life</title>
<link rel="stylesheet" href="https://fonts.googleapis.com/css2?family=Questrial&family=Oswald:wght@300;400&family=Montserrat:wght@600&display=swap">
<style>
  :root {
    --ink-black: #050505;
    --nav-text: #c9c9c9;
    --nav-active: #4d9fe6;
    --brand-blue: #1557b5;
    --heading-grey: #7a7a7a;
    --body-text: #5a5a5a;
    --card-text: #666666;
    --slogan-red: #e0232b;
    --panel-light: #f4f4f4;
    --footer-link: #8c8c8c;
    --call-orange: #f2a21d;
    --footer-white: #e8e8e8;
  }
  * { margin: 0; padding: 0; box-sizing: border-box; }
  html, body { width: 1004px; height: 1200px; overflow: hidden; background: #ffffff; }
  body { position: relative; font-family: Arial, Helvetica, sans-serif; }

  .site-header {
    position: absolute; left: 0; top: 0; width: 1004px; height: 110px;
    background: radial-gradient(ellipse 260px 140px at 280px 10px, #3a3a3a 0%, rgba(0,0,0,0) 70%),
                linear-gradient(#111 0%, var(--ink-black) 100%);
    border-bottom: 1px solid #777;
  }
  .brand { position: absolute; left: 50px; top: 22px; display: flex; align-items: center; gap: 17px; }
  .brand-mark { width: 68px; height: 68px; border-radius: 50%; background: #2a6fd0; }
  .brand-name { font-family: "Questrial", sans-serif; font-size: 30px; color: #ffffff; }

  .main-nav { position: absolute; top: 46px; left: 0; width: 1004px; }
  .main-nav a {
    position: absolute; font-family: "Questrial", sans-serif; font-size: 12.6px;
    color: var(--nav-text); text-decoration: none; letter-spacing: 0.1px;
  }
  .main-nav a.is-active { color: var(--nav-active); }

  .page-band {
    position: absolute; left: 0; top: 111px; width: 1004px; height: 60px;
    background: linear-gradient(#dcdcdc, #ffffff);
  }

  .hero-frame {
    position: absolute; left: 48px; top: 130px; width: 903px; height: 378px;
    background: linear-gradient(90deg, #cfcfcf 0, var(--panel-light) 8px, #ffffff 50%, var(--panel-light) calc(100% - 8px), #cfcfcf 100%);
    border-radius: 3px;
  }
  .hero-visual {
    position: absolute; left: 96px; top: 18px; width: 730px; height: 290px;
    background: linear-gradient(100deg, #e6ecf5 0%, #c9d8ee 50%, #eef1f6 100%);
    border-radius: 2px;
  }
  .hero-slogan {
    position: absolute; left: 330px; top: 321px;
    font-family: "Questrial", sans-serif; font-size: 31px; color: var(--slogan-red); white-space: nowrap;
  }
  .hero-arrow {
    position: absolute; top: 160px; width: 59px; height: 59px; border-radius: 4px;
    background: rgba(215,215,215,0.85); display: flex; align-items: center; justify-content: center;
  }
  .hero-arrow.prev { left: 16px; }
  .hero-arrow.next { right: 16px; }
  .hero-shadow {
    position: absolute; left: 90px; top: 508px; width: 825px; height: 26px;
    background: radial-gradient(ellipse 50% 100% at 50% 0%, rgba(0,0,0,0.55), rgba(0,0,0,0) 100%);
  }

  .welcome { position: absolute; left: 48px; top: 549px; width: 905px; }
  .welcome h1 { font-family: "Oswald", sans-serif; font-weight: 300; font-size: 24px; color: var(--heading-grey); line-height: 32px; }
  .welcome h1 strong { font-weight: 400; color: var(--brand-blue); }
  .welcome p { font-size: 13px; line-height: 20.3px; color: var(--body-text); margin-top: 6px; }
  .welcome p + p { margin-top: 20px; }

  .divider {
    position: absolute; left: 48px; top: 740px; width: 903px; height: 5px;
    background: repeating-linear-gradient(135deg, #d8d8d8 0 1px, #f2f2f2 1px 3px);
  }

  .feature { position: absolute; top: 778px; width: 290px; height: 300px; }
  .feature h2 { font-family: "Montserrat", sans-serif; font-weight: 600; font-size: 16px; color: var(--brand-blue); letter-spacing: 0.2px; margin-left: 1px; }
  .feature-card { position: absolute; left: 4px; top: 30px; width: 278px; height: 232px; }
  .feature-card svg.card-shape { position: absolute; left: 0; top: 0; }
  .feature-photo { position: absolute; left: 14px; top: 15px; width: 233px; height: 101px; }
  .feature-card p { position: absolute; left: 15px; top: 134px; width: 236px; font-size: 11.2px; line-height: 18.4px; color: var(--card-text); }
  .feature-link {
    position: absolute; right: 26px; top: 277px; font-size: 11.5px; color: var(--card-text); text-decoration: none;
    display: flex; align-items: center; gap: 4px;
  }

  .site-footer {
    position: absolute; left: 0; top: 1120px; width: 1004px; height: 80px;
    background: radial-gradient(ellipse 300px 120px at 260px 80px, #333 0%, rgba(0,0,0,0) 70%), #0b0b0b;
  }
  .footer-nav { position: absolute; left: 49px; top: 16px; font-size: 11px; color: var(--footer-link); }
  .footer-nav a { color: var(--footer-link); text-decoration: none; }
  .footer-nav span { margin: 0 11px; }
  .footer-call { position: absolute; left: 49px; top: 41px; font-family: "Questrial", sans-serif; font-size: 13.5px; color: var(--call-orange); }
  .footer-copy { position: absolute; right: 56px; top: 17px; font-size: 11.4px; color: var(--footer-white); }
  .social { position: absolute; right: 53px; top: 40px; display: flex; gap: 6px; }
  .social a { width: 14px; height: 14px; background: #3b7fd0; border-radius: 2px; display: block; }
</style>
</head>
<body>

<header class="site-header">
  <div class="brand">
    <span class="brand-mark"></span>
    <span class="brand-name">BrelloVista</span>
  </div>
  <nav class="main-nav">
    <a href="#" class="is-active" style="left:407px">HOME</a>
    <a href="#" style="left:517px">SOLUTION</a>
    <a href="#" style="left:649px">MEDIA</a>
    <a href="#" style="left:761px">SERVICES</a>
    <a href="#" style="left:889px">ABOUT US</a>
  </nav>
</header>

<div class="page-band"></div>

<section class="hero-frame">
  <div class="hero-visual" role="img" aria-label="Hero photograph: a flat screen monitor with flowers and a blue silk ribbon streaming out to a leaping dancer"></div>
  <p class="hero-slogan">WE BRING BRANDS TO LIFE!</p>
  <a class="hero-arrow prev" href="#" aria-label="Previous slide">
    <svg width="20" height="40" viewBox="0 0 20 40"><polyline points="17,2 3,20 17,38" fill="none" stroke="#ffffff" stroke-width="2"/></svg>
  </a>
  <a class="hero-arrow next" href="#" aria-label="Next slide">
    <svg width="20" height="40" viewBox="0 0 20 40"><polyline points="3,2 17,20 3,38" fill="none" stroke="#ffffff" stroke-width="2"/></svg>
  </a>
</section>
<div class="hero-shadow"></div>

<section class="welcome">
  <h1>Welcome to <strong>BRELLO VISTA</strong></h1>
  <p>Lorem Ipsum is simply dummy text of the printing and typesetting industry. Lorem Ipsum has been the industry's standard dummy text ever since the 1500s, when an unknown printer took a galley of type and scrambled it to make a type specimen book.</p>
  <p>It has survived not only five centuries, but also the leap into electronic typesetting, remaining essentially unchanged. It was popularised in the 1960s with the release of Tessaline sheets containing Lorem Ipsum passages, and more recently with desktop publishing software like Quorvel PageSet including versions of Lorem Ipsum</p>
</section>

<div class="divider"></div>

<section class="feature" style="left:48px">
  <h2>WHAT IS BRELLO VISTA?</h2>
  <div class="feature-card">
    <svg class="card-shape" width="278" height="232" viewBox="0 0 278 232">
      <defs>
        <radialGradient id="cardFace" cx="50%" cy="45%" r="70%"><stop offset="0" stop-color="#ffffff"/><stop offset="0.7" stop-color="#f6f6f6"/><stop offset="1" stop-color="#dcdcdc"/></radialGradient>
      </defs>
      <rect x="0" y="0" width="261" height="232" fill="url(#cardFace)"/>
      <polygon points="261,0 278,16 278,216 261,232" fill="#c8c8c8"/>
    </svg>
    <div class="feature-photo" role="img" aria-label="Business team standing together in a bright glass office" style="background:linear-gradient(90deg,#c9d9e8,#a9c2da 50%,#d8e4ee)"></div>
    <p>Lorem Ipsum is simply dummy text of the printing and typesetting industry. Lorem Ipsum has been the industry's standard dummy text ever since the 1500s.</p>
  </div>
  <a class="feature-link" href="#">Read more <svg width="5" height="7"><polygon points="0,0 5,3.5 0,7" fill="#888"/></svg></a>
</section>

<section class="feature" style="left:363px">
  <h2>HOW CAN WE HELP YOU?</h2>
  <div class="feature-card" style="left:0">
    <svg class="card-shape" width="278" height="232" viewBox="0 0 278 232">
      <rect x="0" y="0" width="261" height="232" fill="url(#cardFace)"/>
      <polygon points="261,0 278,16 278,216 261,232" fill="#c8c8c8"/>
    </svg>
    <div class="feature-photo" role="img" aria-label="Several hands linked together in a circle" style="background:linear-gradient(90deg,#e9e9e9,#d2b299 50%,#e6e6e6)"></div>
    <p>Lorem Ipsum is simply dummy text of the printing and typesetting industry. Lorem Ipsum has been the industry's standard dummy text ever since the 1500s.</p>
  </div>
  <a class="feature-link" href="#" style="right:30px">Read more <svg width="5" height="7"><polygon points="0,0 5,3.5 0,7" fill="#888"/></svg></a>
</section>

<section class="feature" style="left:673px">
  <h2>CONTACT US NOW</h2>
  <div class="feature-card" style="left:1px">
    <svg class="card-shape" width="278" height="232" viewBox="0 0 278 232">
      <rect x="0" y="0" width="261" height="232" fill="url(#cardFace)"/>
      <polygon points="261,0 278,16 278,216 261,232" fill="#c8c8c8"/>
    </svg>
    <div class="feature-photo" role="img" aria-label="Business people meeting across a table" style="background:linear-gradient(90deg,#b8c4cf,#dcd2c2 55%,#c7d2da)"></div>
    <p>Lorem Ipsum is simply dummy text of the printing and typesetting industry. Lorem Ipsum has been the industry's standard dummy text ever since the 1500s.</p>
  </div>
  <a class="feature-link" href="#" style="right:22px">Contact us <svg width="5" height="7"><polygon points="0,0 5,3.5 0,7" fill="#888"/></svg></a>
</section>

<footer class="site-footer">
  <nav class="footer-nav">
    <a href="#">Home</a><span>|</span><a href="#">Solution</a><span>|</span><a href="#">Media</a><span>|</span><a href="#">Services</a><span>|</span><a href="#">About us</a>
  </nav>
  <p class="footer-call">Call Today!: 555-013-2290</p>
  <p class="footer-copy">Copyright © 2011 Brello Vista.&nbsp; All Rights Reserved.</p>
  <div class="social">
    <a href="#" aria-label="Social profile"></a>
    <a href="#" aria-label="Social profile"></a>
    <a href="#" aria-label="Social profile"></a>
  </div>
</footer>

</body>
</html>
```